Ridgewell Stonecraft Construction Needs business card

Hey we are in need of business card designs. I have upload our logo as a guideline, but free feel to run with it or come up with something unique.
Pls have fun with it and be creative. the name says it all!
i will give some directions after i see a few entries..
Logo source file has been uploaded..
Hey because of the logo is so colourful already.
Can we have a few submissions with less colour.
Also we are looking for clever/hidden/descriptive business card.

```html
<!DOCTYPE html>
<html lang="en">
<head>
<meta charset="utf-8">
<title>Ridgewell Stonecraft Construction – Business Card</title>
<link rel="stylesheet" href="https://fonts.googleapis.com/css2?family=Montserrat:wght@600;700&family=Quicksand:wght@400;500&display=swap">
<style>
  :root {
    --bg-light: #9a9a9a;
    --bg-dark: #4f4f4f;
    --card: #ffffff;
    --ink: #111111;
    --ink-soft: #3a3a3a;
    --brand-grey: #5a5a5a;
    --rule: #3d3d3d;
    --accent-blue: #2b8fd6;
  }
  * { box-sizing: border-box; margin: 0; padding: 0; }
  html, body { width: 1200px; height: 1000px; overflow: hidden; }
  body {
    position: relative;
    background: radial-gradient(ellipse at 45% 45%, var(--bg-light) 0%, var(--bg-dark) 75%);
    font-family: "Quicksand", sans-serif;
  }
  .card {
    position: absolute;
    width: 500px;
    height: 300px;
    background: var(--card);
    box-shadow: 0 18px 40px rgba(0,0,0,0.35);
  }
  /* Front */
  .card-front { left: 95px; top: 90px; }
  .front-brand {
    position: absolute;
    left: 0; right: 0; top: 50%;
    transform: translateY(-50%);
    display: flex;
    flex-direction: column;
    align-items: center;
    gap: 14px;
  }
  .front-mark {
    width: 56px; height: 56px;
    background: var(--brand-grey);
  }
  .front-name {
    font-family: "Montserrat", sans-serif;
    font-weight: 700;
    font-size: 30px;
    letter-spacing: 0.5px;
    color: var(--brand-grey);
    text-align: center;
    line-height: 1.15;
  }
  /* Back */
  .card-back { left: 605px; top: 520px; }
  .back-mark {
    position: absolute;
    left: 40px; top: 30px;
    width: 116px; height: 150px;
  }
  .holder {
    position: absolute;
    right: 34px; top: 72px;
    text-align: right;
  }
  .holder-name {
    font-family: "Montserrat", sans-serif;
    font-weight: 700;
    font-size: 28px;
    color: var(--ink);
    letter-spacing: 0.5px;
  }
  .holder-position {
    font-size: 20px;
    font-weight: 500;
    color: var(--ink-soft);
    margin-top: 2px;
  }
  .divider {
    position: absolute;
    left: 0; right: 0; top: 164px;
  }
  .divider span {
    display: block;
    height: 4px;
    background: var(--rule);
    margin-bottom: 5px;
  }
  .contact {
    position: absolute;
    left: 168px; top: 200px;
    display: grid;
    grid-template-columns: auto auto;
    column-gap: 12px;
    row-gap: 2px;
    align-items: baseline;
  }
  .contact-label {
    font-size: 22px;
    font-weight: 400;
    letter-spacing: 2px;
    color: var(--ink-soft);
  }
  .contact-value {
    font-family: "Montserrat", sans-serif;
    font-weight: 600;
    font-size: 13px;
    color: var(--ink);
  }
</style>
</head>
<body>
  <section class="card card-front" aria-label="Card front">
    <div class="front-brand">
      <div class="front-mark"></div>
      <div class="front-name">Ridgewell Stonecraft<br>Construction</div>
    </div>
  </section>

  <section class="card card-back" aria-label="Card back">
    <svg class="back-mark" viewBox="0 0 116 150" aria-hidden="true">
      <rect x="14" y="14" width="88" height="122" fill="none" stroke="var(--accent-blue)" stroke-width="3"/>
    </svg>
    <div class="holder">
      <div class="holder-name">NAME HERE</div>
      <div class="holder-position">Position</div>
    </div>
    <div class="divider"><span></span><span></span></div>
    <div class="contact">
      <span class="contact-label">Office:</span><span class="contact-value">(515) 555 0142</span>
      <span class="contact-label">Mobile:</span><span class="contact-value">(510) 555 0187</span>
      <span class="contact-label">Email:</span><span class="contact-value">NAME@RIDGEWELLSTONE.COM</span>
    </div>
  </section>
</body>
</html>
```